Brindle Capital and Investments

Create a simple business card design using the logos attached. Make it similar but not exact to the reference photo. Brand guidelines are also included.

```html
<!DOCTYPE html>
<html lang="en">
<head>
<meta charset="utf-8">
<title>Brindle Capital – Business Card</title>
<link rel="stylesheet" href="https://fonts.googleapis.com/css2?family=Poppins:wght@400;500;700&display=swap">
<style>
  :root {
    --navy: #0a0f3d;
    --copper: #b0561c;
    --ink: #2b2f45;
    --paper: #ffffff;
    --stage: #e9e8e6;
    --rule: #6b6f85;
  }
  * { margin: 0; padding: 0; box-sizing: border-box; }
  html, body { width: 1200px; height: 900px; overflow: hidden; }
  body {
    background: var(--stage);
    font-family: "Poppins", sans-serif;
    position: relative;
  }
  .card {
    position: absolute;
    left: 280px;
    width: 640px;
    height: 366px;
    border-radius: 34px;
    box-shadow: 0 10px 28px rgba(0,0,0,0.18);
    overflow: hidden;
  }
  /* back side */
  .card--back { top: 48px; background: var(--navy); }
  .back-brand {
    position: absolute;
    right: 60px;
    top: 150px;
    font-weight: 700;
    font-size: 15px;
    letter-spacing: 2px;
    color: var(--paper);
  }
  .back-tagline {
    position: absolute;
    right: 60px;
    bottom: 52px;
    width: 480px;
    text-align: right;
    font-size: 12.5px;
    line-height: 1.5;
    color: var(--copper);
  }
  /* front side */
  .card--front {
    top: 486px;
    background: linear-gradient(100deg, #f1f1f3 0%, var(--paper) 60%, #f6f6f7 100%);
  }
  .front-brand {
    position: absolute;
    right: 56px;
    top: 58px;
    display: flex;
    align-items: center;
    gap: 12px;
  }
  .front-brand__dot {
    width: 14px; height: 14px;
    border-radius: 50%;
    background: var(--copper);
  }
  .front-brand__name {
    font-weight: 700;
    font-size: 26px;
    letter-spacing: 3px;
    color: var(--navy);
  }
  .person {
    position: absolute;
    left: 56px;
    top: 180px;
  }
  .person__name {
    font-weight: 700;
    font-size: 20px;
    color: var(--navy);
    letter-spacing: 0.3px;
  }
  .person__role {
    font-size: 17px;
    color: var(--copper);
    margin-top: -2px;
  }
  .contacts {
    position: absolute;
    left: 56px;
    bottom: 42px;
    list-style: none;
    font-size: 15px;
    color: var(--ink);
    line-height: 1.65;
  }
  .contacts li { display: flex; align-items: center; gap: 10px; }
  .contacts svg { width: 15px; height: 15px; flex: none; }
  .address {
    position: absolute;
    left: 368px;
    bottom: 72px;
    padding-left: 18px;
    border-left: 1.5px solid var(--rule);
    font-size: 15px;
    line-height: 1.45;
    color: var(--ink);
  }
</style>
</head>
<body>

<section class="card card--back" aria-label="Card back">
  <div class="back-brand">BRINDLE CAPITAL</div>
  <p class="back-tagline">Winning the race means delivering strong, dependable returns while building enduring relationships grounded in trust, discipline, and performance.</p>
</section>

<section class="card card--front" aria-label="Card front">
  <div class="front-brand">
    <span class="front-brand__dot"></span>
    <span class="front-brand__name">BRINDLE CAPITAL</span>
  </div>

  <div class="person">
    <div class="person__name">JOHN SMITH</div>
    <div class="person__role">Director</div>
  </div>

  <ul class="contacts">
    <li>
      <svg viewBox="0 0 16 16" aria-hidden="true"><path fill="var(--navy)" d="M3.6 1.5l2.2 2.6-1.3 1.6c.9 2 2.4 3.5 4.4 4.4l1.6-1.3 2.6 2.2-1.3 2.2C6.4 13.3 2.7 9.6 1.4 2.8z"/></svg>
      300-200-9000
    </li>
    <li>
      <svg viewBox="0 0 16 16" aria-hidden="true"><rect x="1" y="3" width="14" height="10" fill="var(--navy)"/><path d="M1 3.5l7 5 7-5" stroke="#fff" stroke-width="1.4" fill="none"/></svg>
      info@brindlecapital.com
    </li>
    <li>
      <svg viewBox="0 0 16 16" aria-hidden="true"><g fill="none" stroke="var(--navy)" stroke-width="1.3"><circle cx="8" cy="8" r="6.5"/><ellipse cx="8" cy="8" rx="2.8" ry="6.5"/><path d="M1.5 8h13M2.5 4.8h11M2.5 11.2h11"/></g></svg>
      www.brindlecapital.com
    </li>
  </ul>

  <address class="address" style="font-style:normal">
    00 dummy city<br>dummy place 0000
  </address>
</section>

</body>
</html>
```